Web Page for Kestrel | ||
Marketing & Admin | ||
Energy | ||
will be www.kestrelfuels-example.com | ||
Kestrel Energy, LLC is a Exploration & Production company drilling oil and gas wells. | ||
Please us our Logo and colors that we had done at this site in Dec 2010. Do not use pictures of people. Would rather use our Logo and color than pictures. | ||
Cutting-Edge Unique/Creative Professional Conservative Exciting Sophisticated Corporate Elegant Traditional Masculine |
top | ||
www.vandrillex-example.com | ||
www.tarnwickog-example.com | ||
Just to see the look, you can use "selective" drilling rig pictures or pumping units but very few and not for all the the contest pages. We will have 2 additional pages at first but would like to be able to add additional in the future. | ||

```html
<!DOCTYPE html>
<html lang="en">
<head>
<meta charset="utf-8">
<title>Kestrel Energy LLC</title>
<link rel="stylesheet" href="https://fonts.googleapis.com/css2?family=Arimo:wght@400;700&display=swap">
<style>
  :root {
    --page-bg: #e9e9e9;
    --page-glow: #ffffff;
    --ink: #1e1e1e;
    --nav-green: #3c9a1f;
    --nav-green-dark: #2c7a12;
    --sky-deep: #1f74c4;
    --sky-light: #8ec8f0;
    --banner-bar: #1a5fa6;
    --panel-dark: #5b5b5b;
    --panel-dark-edge: #4a4a4a;
    --panel-light: #f4f4f4;
    --contact-blue: #2a6db5;
    --field-bg: #e2e2e2;
    --field-edge: #c6c6c6;
    --button-blue: #1f6fc6;
    --footer-bg: #3f3f3f;
    --footer-top: #4a4a4a;
    --footer-text: #ffffff;
  }
  * { box-sizing: border-box; margin: 0; padding: 0; }
  html, body { width: 1200px; height: 1047px; overflow: hidden; }
  body {
    position: relative;
    font-family: "Arimo", Arial, sans-serif;
    color: var(--ink);
    background: radial-gradient(ellipse 700px 480px at 600px 420px, var(--page-glow), var(--page-bg));
  }

  /* Header */
  .brand {
    position: absolute; left: 114px; top: 20px;
    display: flex; align-items: center; gap: 12px;
  }
  .brand-dot { width: 52px; height: 52px; border-radius: 50%; background: var(--ink); }
  .brand-name { font-size: 29px; font-weight: 700; color: var(--ink); letter-spacing: -0.3px; }

  .main-nav {
    position: absolute; top: 29px; left: 668px;
    display: flex; align-items: center; gap: 20px;
    font-size: 13px; font-weight: 700;
  }
  .main-nav a { color: var(--ink); text-decoration: none; }
  .main-nav a.is-current {
    background: linear-gradient(var(--nav-green), var(--nav-green-dark));
    color: #fff; padding: 8px 20px; border-radius: 4px;
  }

  /* Banner */
  .hero {
    position: absolute; left: 119px; top: 76px; width: 948px; height: 370px;
    border: 3px solid #fff; box-shadow: 0 0 4px rgba(0,0,0,0.35);
    overflow: hidden;
  }
  .hero-photo {
    position: absolute; inset: 0;
    background:
      linear-gradient(90deg, rgba(235,240,244,0.9) 0%, rgba(210,222,232,0.75) 30%, rgba(120,175,220,0) 55%),
      linear-gradient(180deg, var(--sky-deep) 0%, var(--sky-light) 100%);
  }
  .hero-title {
    position: absolute; left: 574px; top: 36px; width: 374px; height: 58px;
    background: var(--banner-bar);
    color: #fff; font-size: 31px; font-weight: 700;
    padding: 11px 0 0 14px;
  }
  .hero-tagline {
    position: absolute; left: 587px; top: 128px;
    color: #fff; font-size: 23px; font-weight: 700; line-height: 40px;
  }

  /* Welcome panel */
  .welcome {
    position: absolute; left: 119px; top: 457px; width: 702px; height: 353px;
    background: var(--panel-dark); border: 2px solid var(--panel-dark-edge);
    color: #fff; padding: 12px 14px;
  }
  .welcome h1 {
    font-size: 21px; font-weight: 400; display: inline-block;
    border-bottom: 1px solid #fff; padding-bottom: 1px; margin-bottom: 10px;
  }
  .welcome-photo {
    float: right; width: 212px; height: 158px; margin: 30px 22px 4px 14px;
    border: 2px solid #8a8a8a;
    background: linear-gradient(180deg, #2f5ea8 0%, #7ea6d8 55%, #b9a66b 75%, #7d6a38 100%);
  }
  .welcome p { font-size: 11.5px; line-height: 14px; margin-bottom: 14px; }

  /* Contact panel */
  .contact {
    position: absolute; left: 825px; top: 457px; width: 242px; height: 353px;
    background: linear-gradient(var(--panel-light), #e6e6e6);
    border: 2px solid #bdbdbd;
  }
  .contact h2 {
    font-size: 22px; font-weight: 400; color: var(--contact-blue);
    text-align: center; margin-top: 10px;
  }
  .contact h2::after {
    content: ""; display: block; width: 206px; height: 1px; margin: 6px auto 0;
    background: var(--contact-blue);
  }
  .field { position: absolute; left: 14px; font-size: 11px; font-weight: 700; color: #333; }
  .field-box {
    position: absolute; background: var(--field-bg); border: 1px solid var(--field-edge);
    border-radius: 3px;
  }
  .submit {
    position: absolute; left: 64px; top: 316px; width: 106px; height: 30px;
    background: linear-gradient(#3a8ae0, var(--button-blue));
    color: #fff; font-size: 12px; font-weight: 700; border: 0; border-radius: 4px;
    font-family: inherit;
  }

  /* Footer */
  .site-footer {
    position: absolute; left: 0; top: 836px; width: 1200px; height: 211px;
    background: linear-gradient(var(--footer-top), var(--footer-bg));
    color: var(--footer-text); overflow: hidden;
  }
  .footer-col { position: absolute; top: 12px; }
  .footer-col h3 { font-size: 17px; font-weight: 400; margin-bottom: 11px; }
  .footer-col ul { list-style: none; }
  .footer-col li { font-size: 11.5px; font-weight: 700; line-height: 24px; }
  .footer-address { font-size: 11.5px; font-weight: 700; line-height: 15px; }
  .social { display: flex; gap: 26px; margin-top: 2px; }
  .social span { width: 30px; height: 30px; border-radius: 50%; background: #d9d9d9; }
  .social span + span { background: #3b5ea8; border: 2px solid #fff; }
  .footer-ring {
    position: absolute; left: 1017px; top: 22px; width: 170px; height: 170px;
    border-radius: 50%; background: rgba(255,255,255,0.12); border: 6px solid rgba(255,255,255,0.18);
  }
</style>
</head>
<body>

<header class="site-header">
  <div class="brand">
    <span class="brand-dot"></span>
    <span class="brand-name">Kestrel Energy LLC</span>
  </div>
  <nav class="main-nav">
    <a class="is-current" href="#">Home</a>
    <a href="#">About Kestrel Energy</a>
    <a href="#">Site Map</a>
    <a href="#">Contact Us</a>
  </nav>
</header>

<section class="hero">
  <div class="hero-photo" role="img" aria-label="Photograph of large white oil storage tanks under a clear blue sky"></div>
  <div class="hero-title">Kestrel Energy LLC</div>
  <p class="hero-tagline">Exploration &amp; Production<br>company drilling oil and gas<br>wells.</p>
</section>

<main class="welcome">
  <h1>Welcome to Kestrel Enrgy LLC</h1>
  <div class="welcome-photo" role="img" aria-label="Photograph of wind turbines standing in a field under a blue sky"></div>
  <p>Lorem ipsum dolor sit amet, consectetur adipiscing elit. Suspendisse fermentum nunc eget risus gravida quis pellentesque diam semper. In vitae magna ligula, quis pharetra dui. Donec tincidunt tortor at dolor tristique euismod. Cras vestibulum tincidunt cursus. Nam rutrum, urna non feugiat mollis, sapien mi mollis libero, quis tristique dolor arcu sed est. Nulla eget neque ac ante consequat pharetra. Aliquam ac diam quam. In vel libero, commodo lobortis sodales vitae, rutrum sed tellus. Praesent non eros quam, at accumsan ligula. Etiam et mauris sem, id vehicula enim. Quisque pretium tincidunt justo ac fringilla. Donec feugiat, magna vitae tristique convallis, turpis sem viverra tortor, non rhoncus nisi orci eu nibh. Donec ultrices dolor in turpis consectetur in feugiat ligula suscipit. Class aptent taciti sociosqu ad litora torquent per conubia nostra, per inceptos himenaeos. Nam varius ultrices ante ac sodales. Mauris mauris sem, eleifend nec iaculis a, facilisis non tellus.</p>
  <p>Suspendisse et nisi libero. Fusce nec pulvinar nisl. Curabitur eget dapibus ligula. Fusce sed enim a felis vestibulum consectetur id eu purus. Lorem ipsum dolor sit amet, consectetur adipiscing elit. Ut aliquam eleifend turpis, nam velit lacus, sodales eget facilisis et, ultrices non neque.</p>
</main>

<aside class="contact">
  <h2>Contact Us</h2>
  <span class="field" style="top:70px">Name:</span>
  <span class="field-box" style="left:58px; top:64px; width:170px; height:24px"></span>
  <span class="field" style="top:132px">Email:</span>
  <span class="field-box" style="left:58px; top:126px; width:170px; height:24px"></span>
  <span class="field" style="top:198px">Message:</span>
  <span class="field-box" style="left:78px; top:196px; width:150px; height:106px"></span>
  <button class="submit" type="button">SUBMIT</button>
</aside>

<footer class="site-footer">
  <div class="footer-col" style="left:107px">
    <h3>Quick Links</h3>
    <ul>
      <li>Home</li><li>About Us</li><li>Strategy</li>
      <li>Investor Relations</li><li>Environmental Health</li><li>Contact Us</li>
    </ul>
  </div>
  <div class="footer-col" style="left:333px">
    <h3>Know About Kestrel Energy</h3>
    <ul>
      <li>What is Kestrel Energy</li><li>Privacy Policy</li><li>Kestrel Energy World wide</li>
      <li>Kestrel Energy Fectors</li><li>Main Fectors of Energy</li><li>Our Branches</li>
    </ul>
  </div>
  <div class="footer-col" style="left:618px">
    <h3>Contact Us</h3>
    <p class="footer-address" style="margin-top:14px">Kestrel Energy LLC<br>PO BOX 1234<br>Lorem, Us 192512</p>
  </div>
  <div class="footer-col" style="left:816px">
    <h3>Follow Us On</h3>
    <div class="social"><span></span><span></span></div>
  </div>
  <div class="footer-ring"></div>
</footer>

</body>
</html>
```